Need App for Impact Related Events

My app is to help with internal events. When you enter the prompted event code the next screen shows you everyone currently at the event. It will give you the ability to Start a conversation with someone you met at that event, or signal it is your turn to send a message. The next screen is a message thread with that person. I am looking for a design that incorporates the colors and ‘feel good’ emotion of our logo. I have pieced together a pretty good interpretation of what I’m looking for in the attached mockup by slicing and dicing designs. I also attached our logo mascot.Screens (see attached mockups)

Note 1: I do not like the picture on the screen used in screen one because it makes it seem like a dating app. I attached an alternative photo that can be used or present different ideas.

Note 2: On the login/signup screen (screen 2) I need an additional first and last name for login, you can try to fit this on one login screen or present a two step signup screen where that is presented in the second screen.

READ MOCKUP GUIDELINES UNDER Must Haves

Target Market(s)

People attending internal social impact events

Industry/Entity Type

Charity

Font styles to use
Sans Serif

Colors
86cfc6

Requirements
Must have
• Follow the screen mockups attached to project
• PLEASE READ
• I have provided a relatively close design of what I’m looking for in the mockups. Some screens need to be followed more closely to my design mockup than other. I have listed a guide below how how closely you should follow my mockup design exactly. Overall I would like to see some ideas of incorporating a few accent colors so it doesn’t appear SO Blue. I also attached some app inspiration designs I found from around the web
• Screen Mockup Guideline Follow %
• Screen 1: 65% - mostly on target, would like to see ways to make it not SO Blue and possibly creative places to add some explainer text describing the app
• Screen 2: 50% - general design idea is here, but more open
• Screen 3: 35% - a lot more room for design influence
• Screen 4: 70% - mostly on target, a little room for design influence/color scheme ideas
• Screen 5-6: 25% - a lot of room for design change/ideas/influence
• Screen 7-8: 80% - already very close to what I need, maybe open to slight sizing and color scheme ideas
• Screen 9: 15% - the most open for influence, only the general functionality of the screen is communicated here
Nice to have
• Please Read Mockup Guideline above. In large part I am looking for something to use some nice accent colors so it is not overwhelmingly blue and bring the whole design into a seamless style.
Should not have

```html
<!DOCTYPE html>
<html lang="en">
<head>
<meta charset="utf-8">
<title>Message Thread</title>
<link href="https://fonts.googleapis.com/css2?family=Nunito+Sans:wght@400;600;700;800&family=Roboto:wght@400&display=swap" rel="stylesheet">
<style>
  :root {
    --teal: #12c9c9;
    --ink: #2c2c2c;
    --muted: #8a8a8a;
    --line: #e6e6e6;
    --bubble-in: #ffffff;
    --screen: #ffffff;
    --kb-bg: #f7f7f7;
    --kb-strip: #ececec;
    --key: #3a3a3a;
    --space: #d7d7d7;
    --enter: #4a86f0;
    --avatar: #8a6a5c;
  }
  * { box-sizing: border-box; margin: 0; padding: 0; }
  html, body { width: 675px; height: 1200px; overflow: hidden; background: var(--screen); }
  body { position: relative; font-family: "Nunito Sans", sans-serif; color: var(--ink); }

  .header { position: absolute; left: 0; top: 0; width: 675px; height: 112px; border-bottom: 2px solid var(--line); }
  .back { position: absolute; left: 38px; top: 40px; }
  .video { position: absolute; left: 588px; top: 42px; }
  .contact-name { position: absolute; left: 0; width: 675px; top: 18px; text-align: center; font-size: 31px; font-weight: 700; color: #333; }
  .status { position: absolute; left: 0; width: 675px; top: 56px; text-align: center; font-size: 26px; color: var(--muted); }

  .avatar { position: absolute; width: 64px; height: 64px; border-radius: 50%; background: radial-gradient(circle at 50% 40%, #b08b78, var(--avatar)); }
  .bubble { position: absolute; display: flex; align-items: center; padding: 0 28px; font-size: 21px; }
  .bubble.in { background: var(--bubble-in); border-radius: 8px; box-shadow: 0 2px 8px rgba(0,0,0,0.14); color: #333; }
  .bubble.out { background: var(--teal); border-radius: 8px; color: #fff; font-weight: 700; line-height: 1.45; }
  .time { position: absolute; font-size: 17px; color: #666; }

  .composer { position: absolute; left: 0; top: 643px; width: 675px; height: 90px; border-top: 2px solid var(--line); background: #fff; }
  .composer .plus { position: absolute; left: 36px; top: 30px; }
  .composer .placeholder { position: absolute; left: 112px; top: 28px; font-size: 25px; color: #777; }
  .composer .send { position: absolute; left: 603px; top: 27px; }

  .keyboard { position: absolute; left: 0; top: 733px; width: 675px; height: 467px; background: var(--kb-bg); font-family: "Roboto", sans-serif; }
  .suggestions { position: absolute; left: 0; top: 0; width: 675px; height: 77px; background: var(--kb-strip); }
  .suggestion { position: absolute; top: 20px; width: 200px; text-align: center; font-size: 29px; color: #444; }
  .divider { position: absolute; top: 20px; width: 2px; height: 38px; background: #c8c8c8; }
  .mic { position: absolute; left: 628px; top: 20px; }
  .key { position: absolute; width: 67.5px; text-align: center; font-size: 36px; color: var(--key); }
  .hint { position: absolute; width: 67.5px; text-align: center; font-size: 15px; color: #555; }
  .small-key { position: absolute; font-size: 25px; color: var(--key); }
  .spacebar { position: absolute; left: 253px; top: 386px; width: 235px; height: 45px; border-radius: 4px; background: var(--space); }
  .enter { position: absolute; left: 591px; top: 381px; width: 56px; height: 56px; border-radius: 50%; background: var(--enter); }
</style>
</head>
<body>

<header class="header">
  <svg class="back" width="26" height="34" viewBox="0 0 26 34"><path d="M20 3 L6 17 L20 31" fill="none" stroke="var(--teal)" stroke-width="3.5" stroke-linecap="round" stroke-linejoin="round"/></svg>
  <div class="contact-name">Dylan Marsh</div>
  <div class="status">Online</div>
  <svg class="video" width="46" height="30" viewBox="0 0 46 30"><rect x="0" y="2" width="30" height="26" rx="3" fill="var(--teal)"/><path d="M32 11 L46 3 V27 L32 19 Z" fill="var(--teal)"/></svg>
</header>

<main class="thread">
  <div class="avatar" style="left:17px;top:146px" role="img" aria-label="Contact profile photo"></div>
  <div class="bubble in" style="left:103px;top:148px;width:355px;height:62px">Hello there,</div>
  <div class="time" style="left:484px;top:170px">12:45</div>

  <div class="time" style="left:204px;top:281px">01:03</div>
  <div class="bubble out" style="left:279px;top:259px;width:357px;height:64px">Hey, What's up!</div>

  <div class="avatar" style="left:17px;top:371px" role="img" aria-label="Contact profile photo"></div>
  <div class="bubble in" style="left:103px;top:372px;width:383px;height:63px">Can I meet you in person?</div>
  <div class="time" style="left:512px;top:394px">01:05</div>

  <div class="time" style="left:131px;top:521px">01:13</div>
  <div class="bubble out" style="left:204px;top:484px;width:432px;height:92px">Yeah sure, I'm here at the entrance<br>near the reception.</div>
</main>

<section class="composer">
  <svg class="plus" width="30" height="30" viewBox="0 0 30 30"><path d="M15 2 V28 M2 15 H28" stroke="var(--teal)" stroke-width="3.5" stroke-linecap="round"/></svg>
  <div class="placeholder">Type a message to send</div>
  <svg class="send" width="34" height="34" viewBox="0 0 34 34"><path d="M31 3 L3 14 L15 19 L20 31 Z" fill="var(--teal)"/><path d="M31 3 L15 19" stroke="#fff" stroke-width="2"/></svg>
</section>

<section class="keyboard">
  <div class="suggestions">
    <div class="suggestion" style="left:50px">Hi</div>
    <div class="divider" style="left:237px"></div>
    <div class="suggestion" style="left:234px">Hello</div>
    <div class="divider" style="left:432px"></div>
    <div class="suggestion" style="left:421px">Howdy</div>
    <svg class="mic" width="26" height="38" viewBox="0 0 26 38"><rect x="7" y="2" width="12" height="22" rx="6" fill="#555"/><path d="M3 18 a10 10 0 0 0 20 0 M13 28 V35" fill="none" stroke="#555" stroke-width="2.5"/></svg>
  </div>

  <div class="hint" style="left:26px;top:92px">1</div>
  <div class="hint" style="left:93.5px;top:92px">2</div>
  <div class="hint" style="left:161px;top:92px">3</div>
  <div class="hint" style="left:228.5px;top:92px">4</div>
  <div class="hint" style="left:296px;top:92px">5</div>
  <div class="hint" style="left:363.5px;top:92px">6</div>
  <div class="hint" style="left:431px;top:92px">7</div>
  <div class="hint" style="left:498.5px;top:92px">8</div>
  <div class="hint" style="left:566px;top:92px">9</div>
  <div class="hint" style="left:633.5px;top:92px">0</div>

  <div class="key" style="left:0;top:108px">q</div>
  <div class="key" style="left:67.5px;top:108px">w</div>
  <div class="key" style="left:135px;top:108px">e</div>
  <div class="key" style="left:202.5px;top:108px">r</div>
  <div class="key" style="left:270px;top:108px">t</div>
  <div class="key" style="left:337.5px;top:108px">y</div>
  <div class="key" style="left:405px;top:108px">u</div>
  <div class="key" style="left:472.5px;top:108px">i</div>
  <div class="key" style="left:540px;top:108px">o</div>
  <div class="key" style="left:607.5px;top:108px">p</div>

  <div class="key" style="left:35px;top:204px">a</div>
  <div class="key" style="left:102.5px;top:204px">s</div>
  <div class="key" style="left:170px;top:204px">d</div>
  <div class="key" style="left:237.5px;top:204px">f</div>
  <div class="key" style="left:305px;top:204px">g</div>
  <div class="key" style="left:372.5px;top:204px">h</div>
  <div class="key" style="left:440px;top:204px">j</div>
  <div class="key" style="left:507.5px;top:204px">k</div>
  <div class="key" style="left:575px;top:204px">l</div>

  <svg style="position:absolute;left:32px;top:302px" width="38" height="40" viewBox="0 0 38 40"><path d="M19 3 L35 21 H26 V32 H12 V21 H3 Z" fill="#555"/><rect x="10" y="36" width="18" height="3" fill="#555"/></svg>
  <div class="key" style="left:101px;top:298px">z</div>
  <div class="key" style="left:168.5px;top:298px">x</div>
  <div class="key" style="left:236px;top:298px">c</div>
  <div class="key" style="left:303.5px;top:298px">v</div>
  <div class="key" style="left:371px;top:298px">b</div>
  <div class="key" style="left:438.5px;top:298px">n</div>
  <div class="key" style="left:506px;top:298px">m</div>
  <svg style="position:absolute;left:602px;top:308px" width="42" height="30" viewBox="0 0 42 30"><path d="M12 2 H40 V28 H12 L1 15 Z" fill="#555"/><path d="M20 9 L32 21 M32 9 L20 21" stroke="#fff" stroke-width="3"/></svg>

  <div class="small-key" style="left:22px;top:393px">?123</div>
  <div class="small-key" style="left:128px;top:388px">,</div>
  <svg style="position:absolute;left:185px;top:392px" width="34" height="34" viewBox="0 0 34 34"><circle cx="17" cy="17" r="14" fill="none" stroke="#555" stroke-width="2.5"/></svg>
  <div class="spacebar"></div>
  <div class="small-key" style="left:532px;top:388px">.</div>
  <div class="enter">
    <svg width="56" height="56" viewBox="0 0 56 56"><path d="M38 18 V30 H18 M25 23 L18 30 L25 37" fill="none" stroke="#fff" stroke-width="3.5" stroke-linecap="round" stroke-linejoin="round"/></svg>
  </div>
</section>

</body>
</html>
```